Laundromat washing machine soap instructions poster

I own a laundromat and need a poster explaining to my customers how to load the soap, bleach and fabric softener into our washing machines. I tried to make a poster on canva but it looks terrible. My Laundromat is called "Suds Harbor" and would like my logo to also be on the poster for branding. I would like the poster to use my blue logo colors to match my brand identity.
Under the photo please include the following text:
" *Please place pods inside the washer"
Thanks
Laundromat

```html
<!DOCTYPE html>
<html lang="en">
<head>
<meta charset="UTF-8">
<title>Where Does the Soap Go? – Suds Harbor</title>
<link href="https://fonts.googleapis.com/css2?family=Bebas+Neue&family=Poppins:wght@800&display=swap" rel="stylesheet">
<style>
  :root {
    --brand-blue: #0897d8;
    --ray-blue: #17a4e2;
    --text-blue: #0d8fd3;
    --arrow-cyan: #1ab0d6;
    --white: #ffffff;
    --tray-grey: #6f7173;
    --tray-light: #a9abad;
  }
  html, body { margin: 0; padding: 0; overflow: hidden; }
  body { width: 927px; height: 1200px; background: var(--white); }
  .poster {
    position: relative;
    width: 927px;
    height: 1200px;
    overflow: hidden;
    background: var(--white);
    font-family: "Bebas Neue", sans-serif;
  }
  .sky {
    position: absolute; left: 0; top: 0; width: 927px; height: 640px;
    background:
      repeating-conic-gradient(from 0deg at 463px 380px,
        var(--brand-blue) 0deg 6deg, var(--ray-blue) 6deg 12deg);
  }
  .art { position: absolute; left: 0; top: 0; width: 927px; height: 1200px; }
  .title-text {
    font-family: "Bebas Neue", sans-serif;
    font-size: 124px;
    fill: var(--white);
  }
  .label {
    position: absolute;
    margin: 0;
    font-weight: 400;
    line-height: 0.82;
    text-align: center;
  }
  .label--light { color: var(--white); font-size: 57px; }
  .label--dark { color: var(--text-blue); font-size: 63px; }
  .label--softener { left: 80px; top: 480px; width: 186px; }
  .label--liquid { left: 660px; top: 432px; width: 220px; font-size: 55px; }
  .label--det-left { left: 20px; top: 756px; width: 210px; }
  .label--det-right { left: 697px; top: 756px; width: 210px; }
  .pods-note {
    position: absolute; left: 0; top: 960px; width: 927px; margin: 0;
    text-align: center;
    font-family: "Poppins", sans-serif; font-weight: 800;
    font-size: 26px; color: var(--text-blue); letter-spacing: -0.3px;
  }
  .brand {
    position: absolute; left: 0; top: 1060px; width: 927px;
    display: flex; justify-content: center; align-items: center; gap: 12px;
  }
  .brand-dot { width: 22px; height: 22px; border-radius: 50%; background: var(--text-blue); }
  .brand-name {
    font-family: "Poppins", sans-serif; font-weight: 800;
    font-size: 36px; color: var(--text-blue); margin: 0;
  }
</style>
</head>
<body>
<main class="poster">
  <div class="sky"></div>

  <svg class="art" width="927" height="1200" viewBox="0 0 927 1200">
    <defs>
      <path id="title-arc" d="M 44 268 Q 463 52 884 262"/>
      <linearGradient id="tray-shade" x1="0" y1="0" x2="0" y2="1">
        <stop offset="0" stop-color="var(--tray-light)"/>
        <stop offset="1" stop-color="var(--tray-grey)"/>
      </linearGradient>
    </defs>

    <!-- wave edge -->
    <path fill="var(--white)" d="M0 616 Q 45 600 90 616 T 180 616 T 270 616 T 360 616 T 450 616 T 540 616 T 630 616 T 720 616 T 810 616 T 900 616 T 990 616 V 1200 H 0 Z"/>

    <!-- title -->
    <text class="title-text"><textPath href="#title-arc" startOffset="50%" text-anchor="middle" textLength="890" lengthAdjust="spacing">WHERE DOES THE SOAP GO?</textPath></text>

    <!-- dispenser photo area -->
    <path role="img" aria-label="Photo of the washer's open soap dispenser drawer with four compartments"
      fill="url(#tray-shade)"
      d="M316 241 H615 L612 552 H702 Q716 552 720 566 L732 900 Q732 933 700 933 H225 Q195 933 196 900 L214 566 Q218 552 232 552 H332 Z"/>

    <!-- softener icon -->
    <g fill="none" stroke="var(--white)" stroke-width="6" transform="translate(173 434)">
      <circle r="7"/>
      <g id="petal"><ellipse cx="0" cy="-21" rx="13" ry="15"/></g>
      <use href="#petal" transform="rotate(72)"/>
      <use href="#petal" transform="rotate(144)"/>
      <use href="#petal" transform="rotate(216)"/>
      <use href="#petal" transform="rotate(288)"/>
    </g>

    <!-- liquid detergent / bleach icons -->
    <g fill="none" stroke="var(--white)" stroke-width="9" stroke-linejoin="round">
      <path d="M672 368 L684 416 H738 L750 368"/>
      <path d="M767 416 L806 356 L845 416 Z"/>
    </g>
    <path fill="var(--white)" d="M722 350 C714 364 704 374 704 384 A12 12 0 0 0 728 384 C728 372 724 362 722 350 Z"/>

    <!-- detergent icons -->
    <g fill="none" stroke="var(--text-blue)" stroke-width="9" stroke-linejoin="round" stroke-linecap="round">
      <path d="M75 696 L87 744 H150 L162 696"/>
      <path d="M118 690 V 722"/>
      <path d="M754 696 L766 744 H829 L841 696"/>
      <path d="M784 690 V 722"/><path d="M797 690 V 722"/><path d="M810 690 V 722"/>
    </g>

    <!-- arrows -->
    <g fill="none" stroke="var(--arrow-cyan)" stroke-width="7" stroke-linecap="round" stroke-linejoin="round">
      <path d="M268 504 Q 365 510 383 618"/>
      <path d="M364 598 L383 622 L397 594"/>
      <path d="M659 504 Q 562 510 544 618"/>
      <path d="M530 594 L544 622 L563 598"/>
      <path d="M203 717 Q 330 700 355 782"/>
      <path d="M331 773 L356 786 L361 758"/>
      <path d="M724 717 Q 597 700 572 782"/>
      <path d="M566 758 L571 786 L596 773"/>
    </g>
  </svg>

  <h2 class="label label--light label--softener">SOFTENER</h2>
  <h2 class="label label--light label--liquid">LIQUID ONLY<br>DETERGENT<br>/ BLEACH</h2>
  <h2 class="label label--dark label--det-left">DETERGENT</h2>
  <h2 class="label label--dark label--det-right">DETERGENT</h2>

  <p class="pods-note">Please place pods inside the washer</p>

  <div class="brand">
    <span class="brand-dot"></span>
    <p class="brand-name">Suds Harbor</p>
  </div>
</main>
</body>
</html>
```